Varnel Group Limited Stationary

We are in need of business card and letterhead designs. We are looking for clean modern designs that complement the style and feel of our logo.

Industry/Entity Type

Business

```html
<!DOCTYPE html>
<html lang="en">
<head>
<meta charset="utf-8">
<title>Varnel Group Limited Stationery</title>
<link rel="stylesheet" href="https://fonts.googleapis.com/css2?family=EB+Garamond:wght@400;500&family=Lato:wght@400;700&display=swap">
<style>
  :root {
    --page-bg: #eceef0;
    --paper: #ffffff;
    --navy: #1d3f73;
    --brand-blue: #1c7ac1;
    --brand-blue-deep: #1565a8;
    --slate: #8b8c8e;
    --slate-deep: #7a7b7d;
    --ink: #333333;
    --ink-soft: #555555;
    --icon-pale: #a9c9e4;
    --shadow: 0 2px 6px rgba(0,0,0,.18);
  }
  * { margin: 0; padding: 0; box-sizing: border-box; }
  html, body { width: 1200px; height: 910px; overflow: hidden; }
  body { background: var(--page-bg); position: relative; font-family: "Lato", Arial, sans-serif; color: var(--ink); }

  .piece { position: absolute; box-shadow: var(--shadow); }

  /* Business cards */
  .card { width: 176px; height: 108px; border-radius: 10px; top: 80px; }
  .card-front { left: 188px; background: var(--paper); font-family: "EB Garamond", Georgia, serif; }
  .card-back-slate { left: 436px; background: linear-gradient(135deg, var(--slate), var(--slate-deep)); }
  .card-back-blue { left: 682px; background: linear-gradient(135deg, var(--brand-blue), var(--brand-blue-deep)); }

  .brand { display: flex; flex-direction: column; align-items: center; color: var(--navy); font-family: "EB Garamond", Georgia, serif; font-weight: 500; text-transform: uppercase; letter-spacing: .3px; }
  .brand-dot { border-radius: 50%; background: var(--navy); }
  .card-front .brand { position: absolute; left: 14px; top: 12px; font-size: 9px; }
  .card-front .brand-dot { width: 14px; height: 14px; margin-bottom: 3px; }

  .holder { position: absolute; right: 14px; top: 33px; text-align: right; color: var(--ink-soft); }
  .holder-name { font-size: 9px; }
  .holder-role { font-size: 6px; margin-top: 2px; }

  .card-contact { position: absolute; bottom: 14px; font-size: 5.5px; line-height: 8px; color: var(--ink-soft); }
  .card-contact.address { left: 14px; }
  .card-contact.online { right: 14px; text-align: right; }

  .social-row { position: absolute; display: flex; }
  .card .social-row { left: 0; right: 0; top: 40px; justify-content: center; gap: 6px; }
  .social-dot { width: 25px; height: 25px; }

  /* Letterhead */
  .letterhead { left: 170px; top: 242px; width: 399px; height: 543px; background: var(--paper); border-radius: 12px; }
  .letterhead .brand { position: absolute; left: 0; right: 0; top: 48px; font-size: 8px; }
  .letterhead .brand-dot { width: 13px; height: 13px; margin-bottom: 2px; }
  .salutation { position: absolute; left: 43px; top: 138px; font-size: 9.5px; color: var(--ink); }
  .letter-body { position: absolute; left: 43px; top: 170px; width: 326px; font-size: 6.6px; line-height: 10.8px; text-align: justify; color: var(--ink-soft); }
  .letter-body p + p { margin-top: 6px; }
  .sign-name { position: absolute; left: 43px; top: 363px; font-size: 9px; font-weight: 700; color: var(--ink); }
  .sign-role { position: absolute; left: 43px; top: 378px; font-size: 5.5px; color: var(--ink-soft); }
  .signature { position: absolute; left: 34px; top: 410px; width: 84px; height: 36px; border-radius: 6px; background: linear-gradient(90deg, #ececec, #f6f6f6); }
  .letter-contact { position: absolute; right: 18px; top: 450px; font-family: "EB Garamond", Georgia, serif; font-size: 5px; line-height: 7.6px; text-align: right; color: var(--ink-soft); }
  .letterhead .social-row { right: 19px; top: 506px; gap: 4px; }
  .letterhead .social-dot { width: 19px; height: 19px; }

  /* Folder */
  .folder { left: 631px; top: 242px; width: 399px; height: 543px; border-radius: 12px; background: linear-gradient(160deg, var(--brand-blue) 0%, var(--brand-blue-deep) 100%); }
</style>
</head>
<body>

<!-- Business card front -->
<section class="piece card card-front">
  <div class="brand"><span class="brand-dot"></span>Varnel Group</div>
  <div class="holder">
    <div class="holder-name">Evan Marlow</div>
    <div class="holder-role">President &amp; CEO</div>
  </div>
  <div class="card-contact address">48 Birchwood Lane East<br>City, Province, Country, Zip Code</div>
  <div class="card-contact online">info@varnelgroup.com<br>www.varnelgroup.com</div>
</section>

<!-- Business card back, slate -->
<section class="piece card card-back-slate" role="img" aria-label="Card back with interlocking circle pattern and social profile links">
  <div class="social-row">
    <svg class="social-dot" viewBox="0 0 25 25"><circle cx="12.5" cy="12.5" r="11.5" fill="#fff"/><circle cx="12.5" cy="12.5" r="9" fill="var(--brand-blue)"/></svg>
    <svg class="social-dot" viewBox="0 0 25 25"><circle cx="12.5" cy="12.5" r="11.5" fill="#fff"/><circle cx="12.5" cy="12.5" r="9" fill="var(--brand-blue)"/></svg>
    <svg class="social-dot" viewBox="0 0 25 25"><circle cx="12.5" cy="12.5" r="11.5" fill="#fff"/><circle cx="12.5" cy="12.5" r="9" fill="var(--brand-blue)"/></svg>
    <svg class="social-dot" viewBox="0 0 25 25"><circle cx="12.5" cy="12.5" r="11.5" fill="#fff"/><circle cx="12.5" cy="12.5" r="9" fill="var(--brand-blue)"/></svg>
    <svg class="social-dot" viewBox="0 0 25 25"><circle cx="12.5" cy="12.5" r="11.5" fill="#fff"/><circle cx="12.5" cy="12.5" r="9" fill="var(--brand-blue)"/></svg>
  </div>
</section>

<!-- Business card back, blue -->
<section class="piece card card-back-blue" role="img" aria-label="Card back with interlocking circle pattern and social profile links">
  <div class="social-row">
    <svg class="social-dot" viewBox="0 0 25 25"><circle cx="12.5" cy="12.5" r="11.5" fill="#fff"/><circle cx="12.5" cy="12.5" r="9" fill="var(--brand-blue)"/></svg>
    <svg class="social-dot" viewBox="0 0 25 25"><circle cx="12.5" cy="12.5" r="11.5" fill="#fff"/><circle cx="12.5" cy="12.5" r="9" fill="var(--brand-blue)"/></svg>
    <svg class="social-dot" viewBox="0 0 25 25"><circle cx="12.5" cy="12.5" r="11.5" fill="#fff"/><circle cx="12.5" cy="12.5" r="9" fill="var(--brand-blue)"/></svg>
    <svg class="social-dot" viewBox="0 0 25 25"><circle cx="12.5" cy="12.5" r="11.5" fill="#fff"/><circle cx="12.5" cy="12.5" r="9" fill="var(--brand-blue)"/></svg>
    <svg class="social-dot" viewBox="0 0 25 25"><circle cx="12.5" cy="12.5" r="11.5" fill="#fff"/><circle cx="12.5" cy="12.5" r="9" fill="var(--brand-blue)"/></svg>
  </div>
</section>

<!-- Letterhead -->
<section class="piece letterhead">
  <div class="brand"><span class="brand-dot"></span>Varnel Group</div>
  <p class="salutation">Dear Mr. Harlan,</p>
  <div class="letter-body">
    <p>Lorem ipsum dolor sit amet, consectetur adipiscing elit. Donec orci purus, luctus vitae dignissim eu, iaculis sed purus. Vivamus faucibus, ipsum nec aliquet viverra, leo mauris condimentum ligula, sit amet sagittis enim ligula quis arcu. Nam egestas tortor id nisi porttitor mattis. In tortor ante, ultricies in suscipit a, tempus non massa. Vivamus et auctor mi. Fusce vel massa nulla. Phasellus nec eros mauris, et scelerisque orci. Donec malesuada orci vitae nulla accumsan porta a id massa. Quisque accumsan iaculis magna sit amet fringilla. Maecenas consequat, magna eget tincidunt semper, odio nibh rutrum mi, id feugiat ante nisi eu risus. Vestibulum nunc orci, rhoncus a placerat in, ultricies in mi. Cras mattis varius eros, vel fringilla nisi suscipit eget.</p>
    <p>Quisque scelerisque sagittis nulla at porttitor. Mauris a justo et tellus interdum tristique. Sed id augue vitae urna euismod commodo aliquet a quam. Pellentesque arcu velit, cursus et malesuada ut, consequat et diam. Nullam erat sem, rhoncus id ullamcorper vitae, rhoncus et arcu. In ultricies ultricies nulla, ut rutrum nisi iaculis at. Donec eu magna a metus ornare faucibus. Fusce aliquet faucibus ultricies. Morbi semper, est id tincidunt gravida, sem arcu adipiscing lacus, ac bibendum nulla leo eu purus. Quisque nec diam sed risus consectetur a cumsan quis nibh. Vestibulum id purus lorem.</p>
  </div>
  <p class="sign-name">Evan Marlow</p>
  <p class="sign-role">Co-Founder &amp; CEO</p>
  <div class="signature" role="img" aria-label="Handwritten signature of Evan Marlow"></div>
  <address class="letter-contact" style="font-style:normal">48 Birchwood Lane East<br>City, Province,<br>Country, Zip Code<br>info@varnelgroup.com<br>www.varnelgroup.com</address>
  <div class="social-row">
    <svg class="social-dot" viewBox="0 0 19 19"><circle cx="9.5" cy="9.5" r="8.5" fill="none" stroke="var(--icon-pale)" stroke-width="1.2"/><circle cx="9.5" cy="9.5" r="6.5" fill="var(--icon-pale)"/></svg>
    <svg class="social-dot" viewBox="0 0 19 19"><circle cx="9.5" cy="9.5" r="8.5" fill="none" stroke="var(--icon-pale)" stroke-width="1.2"/><circle cx="9.5" cy="9.5" r="6.5" fill="var(--icon-pale)"/></svg>
    <svg class="social-dot" viewBox="0 0 19 19"><circle cx="9.5" cy="9.5" r="8.5" fill="none" stroke="var(--icon-pale)" stroke-width="1.2"/><circle cx="9.5" cy="9.5" r="6.5" fill="var(--icon-pale)"/></svg>
    <svg class="social-dot" viewBox="0 0 19 19"><circle cx="9.5" cy="9.5" r="8.5" fill="none" stroke="var(--icon-pale)" stroke-width="1.2"/><circle cx="9.5" cy="9.5" r="6.5" fill="var(--icon-pale)"/></svg>
    <svg class="social-dot" viewBox="0 0 19 19"><circle cx="9.5" cy="9.5" r="8.5" fill="none" stroke="var(--icon-pale)" stroke-width="1.2"/><circle cx="9.5" cy="9.5" r="6.5" fill="var(--icon-pale)"/></svg>
  </div>
</section>

<!-- Presentation folder -->
<section class="piece folder" role="img" aria-label="Blue presentation folder covered in a large white interlocking circle pattern"></section>

</body>
</html>
```